Scrap Metal Company Require Brochure for presentation to prospective client

We are a scrap metal company based in Singapore.
We require a brochure of about 4 pages, 1) Cover Page, 2 and 3 is the material we deal in and services we provide and 4) a backpage.
Brochure will be presented to prospective and selected local supplier to present to them the type of products we deal in and the type of services we provide. Purpose is to convince the prospective client to engage our services and also to sell us their scrap metal.
http://www.pelrowanmetals.com/our-services/for-corporate <- This link is for the intended audience of this brochure.
Designer is welcome to take any images from my website or use their own images in the design. Preferably, should the designer choose to use scrap metal images, please try to mainly use pictures of aluminium scrap, copper scrap, stainless steel scrap and ferrous scrap.
Attached is our company logo and some pictures of the scrap. www.pelrowanmetals.com is our website.
The design should give the audience a feeling of confidence, professionalism, honesty and trust in us.
This brochure is intended to be A4 Sizer
Target Market(s)
Local manufacturing company that does metal fabrication with off-cut scrap during the manufacturing process
Industry/Entity Type
Steel
Look and feel

```html
<!DOCTYPE html>
<html lang="en">
<head>
<meta charset="utf-8">
<title>Pel Rowan Metals – Back Cover</title>
<link rel="stylesheet" href="https://fonts.googleapis.com/css2?family=Mulish:wght@400;700;800&display=swap">
<style>
  :root {
    --copper-dark: #2e160b;
    --copper-mid: #7a3f20;
    --copper-light: #c98a62;
    --gold: #c9951f;
    --gold-bright: #f5c518;
    --panel-light: #ffffff;
    --panel-grey: #d6d6d6;
    --ink: #2b2b2b;
    --tagline-grey: #7a7a7a;
  }
  * { margin: 0; padding: 0; box-sizing: border-box; }
  html, body { width: 849px; height: 1200px; overflow: hidden; background: #fff; }
  .back-cover {
    position: relative;
    width: 849px;
    height: 1200px;
    font-family: "Mulish", Arial, sans-serif;
    color: var(--ink);
  }
  .hero-photo {
    position: absolute;
    left: 0; top: 0;
    width: 849px; height: 786px;
    background:
      radial-gradient(ellipse at 45% 45%, rgba(60,25,10,0.35) 0%, rgba(0,0,0,0) 55%),
      linear-gradient(120deg, var(--copper-mid) 0%, var(--copper-light) 30%, var(--copper-mid) 50%, var(--copper-light) 72%, var(--copper-dark) 100%);
  }
  .gold-rule {
    position: absolute;
    left: 0; top: 786px;
    width: 849px; height: 20px;
    background: linear-gradient(90deg, var(--gold) 0%, var(--gold-bright) 50%, var(--gold) 100%);
  }
  .contact-panel {
    position: absolute;
    left: 0; top: 806px;
    width: 849px; height: 394px;
    background: linear-gradient(90deg, var(--panel-grey) 0%, var(--panel-light) 50%, var(--panel-grey) 100%);
    text-align: center;
  }
  .brand-square {
    position: absolute;
    left: 376px; top: 46px;
    width: 97px; height: 97px;
    border: 3px solid var(--gold);
  }
  .brand-block {
    position: absolute;
    left: 256px; top: 170px;
    width: 340px;
  }
  .brand-name {
    font-size: 30px;
    line-height: 34px;
    font-weight: 800;
    letter-spacing: 2px;
    color: var(--gold);
    text-align: center;
    white-space: nowrap;
  }
  .brand-tagline {
    font-size: 19px;
    line-height: 22px;
    font-weight: 800;
    letter-spacing: 2px;
    color: var(--tagline-grey);
    text-align: right;
  }
  .address, .reach {
    position: absolute;
    left: 0; width: 849px;
    font-size: 19px;
    line-height: 24px;
    font-weight: 400;
    letter-spacing: 0.3px;
  }
  .address { top: 248px; }
  .reach { top: 273px; }
  .website {
    position: absolute;
    left: 0; top: 322px;
    width: 849px;
    font-size: 17px;
    letter-spacing: 0.3px;
  }
</style>
</head>
<body>
  <div class="back-cover">
    <div class="hero-photo" role="img" aria-label="Close-up photograph of bundled bright copper scrap wire"></div>
    <div class="gold-rule"></div>
    <div class="contact-panel">
      <div class="brand-square"></div>
      <div class="brand-block">
        <div class="brand-name">PEL ROWAN METALS</div>
        <div class="brand-tagline">RECYCLING</div>
      </div>
      <p class="address">18, Tampines Loop 4, Singapore 528771</p>
      <p class="reach">+65-90001234 | sales@pelrowanmetals.com</p>
      <p class="website">www.pelrowanmetals.com</p>
    </div>
  </div>
</body>
</html>
```